Pregnancy and Fertility Information Website

Hello Designers,
I need a website which provide tips and information about healthy and happy pregnancy. My website name is Lorvin medical.

The website should provide all the information needed throughout pregnancy and beyond ranging from pregnancy tracking tools and articles about common pregnancy concerns and what to expect during pregnancy,etc.
The details about first trimester, second trimester and third trimester should be highlighted in the website.

Top Navigation
Home, Fertility, Pregnancy basics, Articles, Tips and News

I'm looking for a simple and clean design which involves captivating images and colors but it shouldn't be crowded. The design must be professional and modern. An easy to navigate layout is a must.

Green, violet, blue and light yellow colors are my favorites but i'm open to other options.

Any questions. Kindly ask

Industry/Entity Type

Medical

```html
<!DOCTYPE html>
<html lang="en">
<head>
<meta charset="utf-8">
<title>Lorvin Medical</title>
<link href="https://fonts.googleapis.com/css2?family=Open+Sans:wght@400;600;700&family=Raleway:wght@400;500;600&display=swap" rel="stylesheet">
<style>
:root{
  --navy:#0d1850;
  --navy-dark:#0a1140;
  --green:#8dc21f;
  --violet:#b27fdd;
  --grey-bg:#f2f2f2;
  --text:#1c1c1c;
  --white:#ffffff;
  --contact-bg:#14161c;
}
*{box-sizing:border-box;margin:0;padding:0}
html,body{width:1200px;height:2835px;overflow:hidden}
body{position:relative;font-family:"Open Sans",sans-serif;color:var(--text);background:var(--white)}
.abs{position:absolute}
.topbar{left:0;top:0;width:1200px;height:38px;background:var(--navy-dark);color:var(--white);font-size:12px}
.topbar span{position:absolute;top:11px}
.social{display:flex;gap:6px}
.social i{display:block;width:22px;height:22px;background:#2a6ebb}
.header{left:0;top:38px;width:1200px;height:121px;background:var(--white)}
.brand{left:72px;top:82px;display:flex;align-items:center;gap:10px;font-family:"Raleway",sans-serif;font-weight:600;font-size:22px;color:#2a6ebb}
.brand i{display:block;width:26px;height:26px;border-radius:50%;background:var(--green)}
.nav{right:78px;top:38px;display:flex;gap:36px;font-size:15px;font-weight:600;color:var(--navy)}
.nav a{display:block;padding-top:43px;height:121px;color:inherit;text-decoration:none}
.nav a.active{color:var(--green);border-top:4px solid var(--green);padding-top:39px}
.hero{left:0;top:159px;width:1200px;height:463px;background:linear-gradient(90deg,#eef0f6 0%,#6a7296 30%,#2a3468 55%,#1a2460 100%)}
.hero-title{left:604px;top:236px;width:250px;font-family:"Raleway",sans-serif;font-size:32px;font-weight:600;line-height:46px;color:var(--white);white-space:nowrap}
.card-green{left:866px;top:180px;width:257px;height:211px;background:var(--green);color:var(--white);padding:18px 18px}
.card-green h3{font-family:"Raleway",sans-serif;font-size:20px;font-weight:600;display:inline-block;border-bottom:2px solid var(--white);margin-bottom:12px}
.card-green p{font-size:11px;line-height:17px}
.card-contact{left:607px;top:391px;width:259px;height:210px;background:var(--navy);color:var(--white);padding:22px 18px}
.card-contact h3{font-family:"Raleway",sans-serif;font-size:20px;font-weight:500;margin-bottom:14px}
.card-contact p{font-size:10px;line-height:17px}
.btn-outline{display:block;border:2px solid var(--white);color:var(--white);text-align:center;font-size:14px;width:110px;height:36px;line-height:32px;margin:26px 0 0 58px}
.card-list{left:866px;top:391px;width:257px;height:210px;background:var(--white);padding:20px 18px}
.card-list h3{font-family:"Raleway",sans-serif;font-size:21px;font-weight:600;color:var(--navy);display:inline-block;border-bottom:2px solid var(--navy);margin-bottom:18px}
.card-list li{list-style:none;display:flex;align-items:center;gap:14px;font-size:15px;color:var(--navy);margin-bottom:20px}
.card-list li i{display:block;width:15px;height:15px;border:2px solid var(--navy);position:relative}
.card-list li i::after{content:"";position:absolute;left:3px;top:3px;width:5px;height:5px;background:var(--navy)}
.section-title{left:0;width:1200px;text-align:center;font-family:"Raleway",sans-serif;font-size:30px;font-weight:500}
.rule{left:378px;width:497px;height:4px;background:#d6d6d6}
.rule i{position:absolute;left:153px;top:0;width:183px;height:4px;background:var(--green)}
.about{left:0;top:622px;width:1200px;height:389px;background:var(--violet)}
.about-col{top:748px;font-size:14.5px;line-height:21px;color:var(--white)}
.trimesters{left:0;top:1011px;width:1200px;height:639px;background:var(--grey-bg)}
.tri{width:300px}
.tri-back{position:absolute;left:0;top:0;width:250px;height:240px;background:var(--green);border:2px solid #fff;outline:1px solid #ccc}
.tri-photo{position:absolute;left:16px;top:20px;width:260px;height:231px;background:linear-gradient(90deg,#2a3270 0%,#3a4580 45%,#8b8fa8 70%,#c9c4c4 100%);border:3px solid #fff;outline:1px solid #ccc}
.tri-photo span{position:absolute;left:24px;top:20px;color:var(--white);font-size:22px;font-weight:600;line-height:28px;text-align:center}
.tri p{position:absolute;left:0;top:276px;width:285px;font-size:13.5px;line-height:21px}
.services{left:0;top:1650px;width:1200px;height:467px;background:var(--white)}
.svc{width:280px}
.svc svg{position:absolute;left:0;top:0}
.svc h4{position:absolute;left:68px;top:-4px;font-size:22px;font-weight:400;color:#111;white-space:nowrap}
.svc p{position:absolute;left:68px;top:30px;width:200px;font-size:12px;line-height:17px}
.cta{left:0;top:2117px;width:1200px;height:109px;background:var(--navy)}
.cta-text{left:70px;top:2150px;font-size:30px;color:var(--white);white-space:nowrap}
.cta-btn{left:924px;top:2145px;width:163px;height:52px;border:2px solid var(--white);color:var(--white);text-align:center;line-height:48px;font-size:15px}
.contact{left:0;top:2226px;width:1200px;height:565px;background:linear-gradient(160deg,#1c2029 0%,#111318 50%,#1b1e24 100%)}
.form-lbl{color:var(--white);font-size:15px}
.field{border:2px solid #d8d8d8;background:transparent}
.send{left:522px;top:2584px;width:172px;height:45px;background:var(--green);color:var(--white);text-align:center;line-height:45px;font-size:15px}
.info{color:var(--white);font-size:15px;line-height:26px}
.footer{left:0;top:2791px;width:1200px;height:44px;background:var(--navy);color:var(--white);text-align:center;font-size:14px;line-height:44px}
</style>
</head>
<body>

<div class="abs topbar">
  <span style="left:70px">Have any questions?</span>
  <span style="left:208px">&#9990; +11 555 010 274</span>
  <span style="left:330px">&#9993; hello@lorvinmedical.example</span>
  <div class="abs social" style="left:1019px;top:6px"><i></i><i style="background:#1da1f2"></i><i style="background:#0a66c2"></i></div>
</div>

<div class="abs header"></div>
<div class="abs brand"><i></i>Lorvin Medical</div>
<nav class="abs nav">
  <a class="active">Home</a><a>Fertility</a><a>Pregnancy Basics</a><a>Articles</a><a>Tips and News</a>
</nav>

<div class="abs hero" role="img" aria-label="Photo of a doctor with a pregnant patient in a clinic room"></div>
<h1 class="abs hero-title">Welcome to<br>Lorvin Medical</h1>
<div class="abs card-green">
  <h3>Lorvin Medical</h3>
  <p>Lorem Ipsum Text Here Lorem Ipsum Text Here Lorem Ipsum Text Here Lorem Ipsum Text Here Lorem Ipsum Text Here Lorem Ipsum Text Here Lorem Ipsum Text Here</p>
</div>
<div class="abs card-contact">
  <h3>Contact us</h3>
  <p>Lorvin Medical<br>Level 14, 88 Harbor Lane,<br>Northvale, Victoria 3100<br>Australia</p>
  <span class="btn-outline">Contact</span>
</div>
<div class="abs card-list">
  <h3>Lorem Ipsum :</h3>
  <ul><li><i></i>First Trimester</li><li><i></i>Second Trimester</li><li><i></i>Third Trimester</li></ul>
</div>

<div class="abs about"></div>
<h2 class="abs section-title" style="top:655px;color:var(--white)">Welcome to Lorvin Medical</h2>
<div class="abs rule" style="top:710px;background:#e6e6e6"><i style="background:#333a55"></i></div>
<p class="abs about-col" style="left:70px;width:546px">Lorem Ipsum is simply dummy text of the printing and typesetting industry. Lorem Ipsum has been the industry's standard dummy text ever since the 1500s, when an unknown printer took a galley of type and scrambled it to make a type specimen book.<br><span style="font-size:13px;line-height:20px">Lorem Ipsum is simply dummy text of the printing and typesetting industry. Lorem Ipsum has been the industry's standard dummy text ever since the 1500s, when an unknown printer took a galley of type and scrambled it to make a type specimen book.</span></p>
<p class="abs about-col" style="left:645px;width:465px">Lorem Ipsum is simply dummy text of the printing and typesetting industry. Lorem Ipsum has been the industry's standard dummy text ever since the 1500s, when an unknown printer took a galley of type and scrambled it to make a type specimen book.<br><span style="font-size:13px;line-height:20px">Lorem Ipsum is simply dummy text of the printing and typesetting industry. Lorem Ipsum has been the industry's standard dummy text ever since the 1500s, when an unknown printer took a galley of type and scrambled it to make a type specimen book.</span></p>

<div class="abs trimesters"></div>
<h2 class="abs section-title" style="top:1054px;color:var(--navy)">Lorem Ipsum</h2>
<div class="abs rule" style="top:1109px"><i></i></div>

<div class="abs tri" style="left:70px;top:1176px">
  <div class="tri-back"></div>
  <div class="tri-photo" role="img" aria-label="Photo of an expectant mother in early pregnancy"><span>First<br>Trimester</span></div>
  <p>Lorem Ipsum is simply dummy text of the printing and typesetting industry. Lorem Ipsum has been the industry's standard dummy text ever since the 1500s, when an unknown printer took a galley of type and scrambled it to make a type specimen book.</p>
</div>
<div class="abs tri" style="left:456px;top:1176px">
  <div class="tri-back"></div>
  <div class="tri-photo" role="img" aria-label="Photo of an expectant mother in mid pregnancy"><span>Second<br>Trimester</span></div>
  <p>Lorem Ipsum is simply dummy text of the printing and typesetting industry. Lorem Ipsum has been the industry's standard dummy text ever since the 1500s, when an unknown printer took a galley of type and scrambled it to make a type specimen book.</p>
</div>
<div class="abs tri" style="left:845px;top:1176px">
  <div class="tri-back"></div>
  <div class="tri-photo" role="img" aria-label="Photo of an expectant mother in late pregnancy"><span>Third<br>Trimester</span></div>
  <p>Lorem Ipsum is simply dummy text of the printing and typesetting industry. Lorem Ipsum has been the industry's standard dummy text ever since the 1500s, when an unknown printer took a galley of type and scrambled it to make a type specimen book.</p>
</div>

<div class="abs services"></div>
<h2 class="abs section-title" style="top:1686px;color:var(--navy)">See what we provide for your health</h2>
<div class="abs rule" style="top:1740px;left:363px;width:357px"><i style="left:115px;width:127px"></i></div>

<div class="abs svc" style="left:70px;top:1812px">
  <svg width="48" height="48" viewBox="0 0 48 48"><circle cx="24" cy="14" r="10" fill="#111"/><path d="M4 46c0-12 9-18 20-18s20 6 20 18z" fill="#111"/></svg>
  <h4>Certified doctors</h4><p>Vitae adipiscing turpis. Aenean ligula nibh in, molestie id viverra a, dapibus at dolor.</p>
</div>
<div class="abs svc" style="left:469px;top:1812px">
  <svg width="44" height="48" viewBox="0 0 44 48"><rect x="6" y="6" width="32" height="40" rx="3" fill="none" stroke="#111" stroke-width="3"/><rect x="15" y="2" width="14" height="8" fill="#111"/><path d="M13 20h18M13 28h18M13 36h18" stroke="#111" stroke-width="3"/></svg>
  <h4>Quick visits</h4><p>Vitae adipiscing turpis. Aenean ligula nibh in, molestie id viverra a, dapibus at dolor.</p>
</div>
<div class="abs svc" style="left:854px;top:1812px">
  <svg width="50" height="40" viewBox="0 0 50 40"><rect x="2" y="6" width="46" height="28" rx="3" fill="#111"/><rect x="2" y="12" width="46" height="5" fill="#fff"/><rect x="32" y="24" width="10" height="4" fill="#fff"/></svg>
  <h4>Card payments</h4><p>Vitae adipiscing turpis. Aenean ligula nibh in, molestie id viverra a, dapibus at dolor.</p>
</div>
<div class="abs svc" style="left:70px;top:1979px">
  <svg width="44" height="40" viewBox="0 0 44 40"><path d="M6 4h32l4 12H2z" fill="#111"/><rect x="2" y="16" width="40" height="20" fill="#111"/><rect x="16" y="22" width="12" height="4" fill="#fff"/></svg>
  <h4>Patients history</h4><p>Vitae adipiscing turpis. Aenean ligula nibh in, molestie id viverra a, dapibus at dolor.</p>
</div>
<div class="abs svc" style="left:464px;top:1979px">
  <svg width="50" height="50" viewBox="0 0 50 50"><path d="M6 44C10 20 28 8 48 4 44 26 30 40 12 40z" fill="#111"/><path d="M4 48L30 20" stroke="#fff" stroke-width="2"/></svg>
  <h4>Natural medicine</h4><p>Vitae adipiscing turpis. Aenean ligula nibh in, molestie id viverra a, dapibus at dolor.</p>
</div>
<div class="abs svc" style="left:854px;top:1979px">
  <svg width="46" height="48" viewBox="0 0 46 48"><circle cx="23" cy="26" r="18" fill="none" stroke="#111" stroke-width="3"/><path d="M23 14v12l8 5" stroke="#111" stroke-width="3" fill="none"/><path d="M4 10l8-7M42 10l-8-7" stroke="#111" stroke-width="4"/></svg>
  <h4>Short terms</h4><p>Vitae adipiscing turpis. Aenean ligula nibh in, molestie id viverra a, dapibus at dolor.</p>
</div>

<div class="abs cta"></div>
<p class="abs cta-text">Do you want to visit our clinic? Make an free appointment!</p>
<div class="abs cta-btn">Contact Us</div>

<div class="abs contact" role="img" aria-label="Dark photo of a desk with a laptop, camera and plant"></div>
<h3 class="abs" style="left:70px;top:2273px;color:var(--white);font-size:20px;font-weight:700">Write a message :</h3>
<p class="abs info" style="left:70px;top:2335px;width:370px;font-size:14.5px;line-height:24px">If you got any questions, please do not hesitage to send us a message. We reply within 24 hours.</p>
<p class="abs info" style="left:214px;top:2403px;font-size:14.5px">Our profiles in Social Media:</p>
<div class="abs social" style="left:306px;top:2444px;gap:10px"><i style="width:32px;height:32px"></i><i style="width:32px;height:32px;background:#1da1f2"></i><i style="width:32px;height:32px;background:#0a66c2"></i></div>

<span class="abs form-lbl" style="left:520px;top:2273px">Name :</span>
<span class="abs form-lbl" style="left:720px;top:2273px">Email Address :</span>
<span class="abs form-lbl" style="left:945px;top:2273px">Subject :</span>
<div class="abs field" style="left:520px;top:2304px;width:170px;height:32px"></div>
<div class="abs field" style="left:720px;top:2304px;width:170px;height:32px"></div>
<div class="abs field" style="left:945px;top:2304px;width:168px;height:32px"></div>
<span class="abs form-lbl" style="left:520px;top:2360px">Message :</span>
<div class="abs field" style="left:520px;top:2391px;width:593px;height:151px"></div>
<div class="abs send">Send Message</div>

<div class="abs info" style="left:70px;top:2554px;width:100px">Email :<br>Quick Call :<br>Location :</div>
<div class="abs info" style="left:176px;top:2554px;width:280px">
  <div>&#9993; hello@lorvinmedical.example</div>
  <div>&#9990; +11 555 010 274</div>
  <div style="display:flex;gap:8px"><svg width="12" height="18" viewBox="0 0 12 18" style="margin-top:5px"><path d="M6 0a6 6 0 0 1 6 6c0 5-6 12-6 12S0 11 0 6a6 6 0 0 1 6-6z" fill="#fff"/><circle cx="6" cy="6" r="2.2" fill="#14161c"/></svg><span style="line-height:21px;margin-top:2px">Level 14, 88 Harbor Lane,<br>Northvale, Victoria 3100<br>Australia</span></div>
</div>

<div class="abs footer">&copy; 2017 Lorvin Medical. All Rights Reserved.</div>

</body>
</html>
```